Crust Harbor Hotel Coupon

Would like to design a coupon that is for hotels' staff and to be dropped off at the hotel front office anytime someone calls from a hotel and as a Thank You for hotel staff for recommending us. Coupon value to be $ 2.00. Should say Thank You or Thank you for recommending us. Need our phone number 250 413 6587 on it. Color scheme to be Green and Red as in the attached logo. Coupon to be designed for printing size 3.5 inches high and 7.5 inches wide. Rear should say Fastest Delivery, Favourite Pizza for Sports teams etc. Ask for group deals. Attached logo to be on the coupon. Coupon should say coupon # and space left for us write number

```html
<!DOCTYPE html>
<html lang="en">
<head>
<meta charset="utf-8">
<title>Crust Harbor Hotel Coupon</title>
<link rel="stylesheet" href="https://fonts.googleapis.com/css2?family=Nunito:wght@700;800;900&display=swap">
<style>
  :root {
    --red: #d4101a;
    --red-deep: #b00d14;
    --green: #0f7a36;
    --green-deep: #086329;
    --green-badge: #15953f;
    --lime: #a6c72b;
    --white: #ffffff;
    --ink-green: #0b5e28;
    --page: #f2f2f2;
  }
  * { box-sizing: border-box; margin: 0; padding: 0; }
  html, body { width: 1200px; height: 1200px; overflow: hidden; }
  body {
    background: var(--page);
    font-family: "Nunito", sans-serif;
    position: relative;
  }
  .card {
    position: absolute;
    left: 178px;
    width: 843px;
    height: 393px;
    overflow: hidden;
  }
  .card--front { top: 178px; background: var(--red); }
  .card--back { top: 665px; background: var(--green); }
  .card__pattern { position: absolute; inset: 0; }
  .card--front .card__pattern {
    background: radial-gradient(circle at 210px 230px, #e3141d 0%, var(--red) 40%, var(--red-deep) 100%);
  }
  .card--back .card__pattern {
    background: linear-gradient(180deg, #12803a 0%, var(--green) 100%);
  }
  .shapes { position: absolute; inset: 0; }

  .brand-name {
    position: absolute;
    font-weight: 900;
    color: var(--white);
    text-align: center;
    white-space: nowrap;
    line-height: 1;
  }
  .front__brand { left: 110px; top: 77px; width: 200px; font-size: 29px; }

  .offer {
    position: absolute;
    left: 66px;
    width: 288px;
    text-align: center;
    color: var(--white);
    line-height: 1;
  }
  .offer__amount { top: 160px; font-size: 66px; font-weight: 900; letter-spacing: -1px; }
  .offer__amount sup { font-size: 30px; vertical-align: 28px; }
  .offer__off { top: 218px; font-size: 58px; font-weight: 900; letter-spacing: 2px; }
  .offer__note { top: 288px; font-size: 16px; font-weight: 800; }

  .thanks__title {
    position: absolute;
    left: 410px; width: 360px; top: 146px;
    text-align: center;
    color: var(--white);
    font-size: 66px; font-weight: 900;
    line-height: 1;
    letter-spacing: -0.5px;
  }
  .thanks__ribbon-text {
    position: absolute;
    left: 411px; width: 359px; top: 228px;
    text-align: center;
    color: var(--white);
    font-size: 25px; font-weight: 900;
    line-height: 30px;
  }
  .thanks__ribbon-text .star { color: var(--lime); font-size: 20px; }
  .coupon-number {
    position: absolute;
    left: 479px; top: 284px; width: 221px; height: 26px;
    background: var(--white);
    border-radius: 4px;
    color: var(--ink-green);
    font-size: 17px; font-weight: 900;
    padding-left: 10px;
    line-height: 26px;
  }

  .order__title {
    position: absolute;
    left: 222px; width: 400px; top: 58px;
    text-align: center;
    color: var(--white);
    font-size: 58px; font-weight: 900;
    line-height: 1;
  }
  .order__phone {
    position: absolute;
    left: 267px; width: 308px; top: 135px; height: 42px;
    display: flex; align-items: center; justify-content: center; gap: 6px;
    color: var(--white);
    font-size: 32px; font-weight: 900;
  }
  .feature {
    position: absolute;
    top: 302px;
    width: 170px;
    text-align: center;
    color: var(--white);
    font-size: 16px; font-weight: 800;
    line-height: 16px;
  }
  .back__brand { left: 664px; top: 314px; width: 156px; font-size: 23px; }
</style>
</head>
<body>

<section class="card card--front" aria-label="Coupon front">
  <div class="card__pattern" role="img" aria-label="Faint line-drawn pizza and ingredient pattern on red"></div>
  <svg class="shapes" width="843" height="393" viewBox="0 0 843 393" aria-hidden="true">
    <circle cx="210" cy="232" r="146" fill="var(--green-badge)"/>
    <circle cx="210" cy="232" r="132" fill="none" stroke="var(--lime)" stroke-width="2"/>
    <ellipse cx="210" cy="92" rx="112" ry="40" fill="var(--green-deep)"/>
    <line x1="122" y1="277" x2="298" y2="277" stroke="var(--lime)" stroke-width="2"/>
    <polygon points="411,226 770,226 762,244 770,262 411,262 419,244" fill="var(--green-deep)"/>
  </svg>

  <div class="brand-name front__brand">Crust Harbor</div>
  <div class="offer offer__amount"><sup>$</sup>2.00</div>
  <div class="offer offer__off">OFF</div>
  <div class="offer offer__note">with this coupon</div>

  <h1 class="thanks__title">Thank you</h1>
  <p class="thanks__ribbon-text"><span class="star">★</span> for recommending us <span class="star">★</span></p>
  <div class="coupon-number">Coupon #</div>
</section>

<section class="card card--back" aria-label="Coupon back">
  <div class="card__pattern" role="img" aria-label="Faint line-drawn pizza and ingredient pattern on green"></div>
  <svg class="shapes" width="843" height="393" viewBox="0 0 843 393" aria-hidden="true">
    <path d="M610 393 C680 330 760 300 843 290 L843 393 Z" fill="var(--green-deep)"/>
    <rect x="12" y="12" width="819" height="368" rx="10" fill="none" stroke="var(--lime)" stroke-width="2"/>
    <polygon points="267,135 575,135 565,156 575,177 267,177 277,156" fill="var(--red)"/>
    <g fill="none" stroke="var(--lime)" stroke-width="3">
      <circle cx="268" cy="251" r="38"/>
      <circle cx="418" cy="251" r="38"/>
      <circle cx="570" cy="251" r="38"/>
    </g>
    <g fill="none" stroke="var(--white)" stroke-width="2" stroke-linecap="round">
      <rect x="252" y="241" width="20" height="14" rx="2"/>
      <path d="M272 248 h8 l6 7"/>
      <circle cx="257" cy="262" r="4"/>
      <circle cx="282" cy="262" r="4"/>
      <line x1="240" y1="244" x2="248" y2="244"/>
      <line x1="238" y1="250" x2="248" y2="250"/>
      <ellipse cx="414" cy="255" rx="18" ry="11" transform="rotate(-35 414 255)"/>
      <line x1="407" y1="261" x2="421" y2="249"/>
      <circle cx="432" cy="237" r="7"/>
      <circle cx="563" cy="242" r="7"/>
      <circle cx="577" cy="242" r="7"/>
      <path d="M551 265 c0-10 24-10 24 0 M565 265 c0-10 24-10 24 0"/>
    </g>
  </svg>

  <h2 class="order__title">Order now</h2>
  <div class="order__phone">
    <svg width="24" height="26" viewBox="0 0 24 26" aria-hidden="true">
      <path d="M6 3 L10 8 L7 11 C8 15 10 18 14 20 L17 17 L22 21 L18 25 C9 23 3 15 2 6 Z" fill="var(--white)"/>
    </svg>
    <span>250 413 6587</span>
  </div>

  <p class="feature" style="left:183px">Fastest<br>Delivery</p>
  <p class="feature" style="left:333px">Favourite Pizza<br>for Sports teams</p>
  <p class="feature" style="left:485px">Ask for<br>group deals</p>

  <div class="brand-name back__brand">Crust Harbor</div>
</section>

</body>
</html>
```